Postcard Design

I am promoting a local school tax levy increase. I need a post card that helps market this. I saw a nice one online that someone did and I'd like something similar. I am attaching a picture of it.
Our election is April 7, 2015 and we want people to vote YES on it!
My bullet points will be: Our Children Our District Our Future
Our colors are Kelly Green and Canary but it is not mandatory that the postcards be those colors. I really like the image I sent you.
We also need to have the name of the ballot measure in smaller print under the date on the side which is: "Proposition Cedar Hollow East High School"
We also need it to say: "Advertisement paid for by the Cedar Hollow East High School Election Committee, Marla Kinney Treasurer.
For the back, you can put our name, address, and a picture of our proposed school which is image #2. You can also put: Call Derek Holcomb @ 417-586-1047 for more information or to register for an upcoming Q&A forum.
Our name/Address is: Cedar Hollow East High School Election Committee
2736 County Road 3815
Lindell, MO 65712
You can also include the facebook symbol on our card as we are on facebook and can include our web address as well which is: www.cedarhollowsample.com

Please spell check everything!

Please send me your ideas. I will need postage and address which I will provide once the proof is approved.
Thanks, Derek Holcomb 417-586-1047

```html
<!DOCTYPE html>
<html lang="en">
<head>
<meta charset="utf-8">
<title>Vote Yes Postcard – Cedar Hollow East High School</title>
<link rel="stylesheet" href="https://fonts.googleapis.com/css2?family=Oswald:wght@400;600;700&family=Lato:ital,wght@0,400;0,700;1,400&display=swap">
<style>
  :root {
    --canary: #f4ec33;
    --kelly: #17733d;
    --kelly-dark: #0f5a2e;
    --paper: #ffffff;
    --page: #e9e6e1;
    --photo-sky: #9fc3dd;
    --photo-ground: #8d8a80;
  }
  * { box-sizing: border-box; margin: 0; padding: 0; }
  html, body { width: 861px; height: 1200px; overflow: hidden; }
  body { background: var(--page); position: relative; font-family: 'Lato', sans-serif; }

  /* Front side */
  .card-front {
    position: absolute; left: 63px; top: 52px; width: 727px; height: 563px;
    background: var(--canary); color: var(--kelly);
    box-shadow: 0 4px 12px rgba(0,0,0,.18);
    overflow: hidden;
  }
  .check-badge { position: absolute; left: 44px; top: 76px; width: 205px; height: 205px; }
  .headline {
    position: absolute; left: 276px; top: 50px;
    font-family: 'Oswald', sans-serif; font-weight: 700; line-height: .92;
  }
  .headline .vote { display: block; font-size: 120px; letter-spacing: 1px; }
  .headline .yes { display: block; font-size: 124px; letter-spacing: 12px; }
  .date-rule { position: absolute; left: 556px; top: 58px; width: 5px; height: 262px; background: var(--kelly); }
  .date-block {
    position: absolute; left: 570px; top: 58px; height: 262px;
    writing-mode: vertical-rl; transform: rotate(180deg);
    display: flex; flex-direction: column; justify-content: flex-start;
  }
  .date-block .date {
    font-family: 'Oswald', sans-serif; font-weight: 600; font-size: 84px;
    line-height: 1; letter-spacing: 2px; white-space: nowrap;
  }
  .date-block .measure {
    font-family: 'Oswald', sans-serif; font-weight: 600; font-size: 13px;
    line-height: 1.1; white-space: nowrap; margin-left: 2px;
  }
  .pillars-rule { position: absolute; left: 30px; right: 30px; height: 3px; background: var(--kelly); }
  .pillars-rule.top { top: 352px; }
  .pillars-rule.bottom { top: 428px; }
  .pillars {
    position: absolute; left: 30px; right: 30px; top: 364px;
    display: flex; justify-content: space-between; white-space: nowrap;
    font-family: 'Oswald', sans-serif; font-size: 30px; font-weight: 400; letter-spacing: 2px;
    line-height: 52px;
  }
  .disclaimer {
    position: absolute; right: 34px; top: 446px;
    font-size: 11px; font-style: italic; white-space: nowrap;
  }

  /* Back side */
  .card-back {
    position: absolute; left: 132px; top: 632px; width: 649px; height: 530px;
    background: var(--paper); color: var(--kelly);
    box-shadow: 0 4px 12px rgba(0,0,0,.18);
  }
  .school-photo {
    position: absolute; left: 20px; top: 20px; width: 420px; height: 170px;
    background: linear-gradient(to bottom, var(--photo-sky) 0%, #cfe0ea 55%, var(--photo-ground) 56%, #6f7a5c 100%);
  }
  .social-mark {
    position: absolute; left: 414px; top: 164px; width: 20px; height: 20px;
    background: #3b5a99;
  }
  .stamp-box { position: absolute; right: 28px; top: 26px; width: 96px; height: 104px; border: 2px solid #777; }
  .back-info { position: absolute; left: 24px; top: 206px; width: 430px; }
  .committee { font-size: 18px; font-weight: 700; margin-bottom: 14px; }
  .purpose, .contact, .note { padding-left: 64px; }
  .purpose { font-size: 14px; margin-bottom: 12px; }
  .contact { font-size: 17px; line-height: 1.35; margin-bottom: 12px; color: var(--kelly-dark); }
  .note { font-size: 13.5px; font-style: italic; line-height: 1.3; }
  .web {
    position: absolute; left: 24px; top: 470px; width: 430px;
    font-size: 17px; font-weight: 700; letter-spacing: 1.5px;
    border-bottom: 2px solid var(--kelly); padding-bottom: 6px;
  }
</style>
</head>
<body>
  <section class="card-front" aria-label="Postcard front">
    <svg class="check-badge" viewBox="0 0 200 200" aria-hidden="true">
      <circle cx="100" cy="100" r="98" fill="var(--kelly)"/>
      <circle cx="100" cy="100" r="84" fill="none" stroke="var(--paper)" stroke-width="5"/>
      <path d="M48 104 L84 140 L154 66" fill="none" stroke="var(--paper)" stroke-width="24" stroke-linecap="square" stroke-linejoin="miter"/>
    </svg>
    <h1 class="headline"><span class="vote">VOTE</span><span class="yes">YES</span></h1>
    <div class="date-rule"></div>
    <div class="date-block">
      <span class="date">APRIL 7</span>
      <span class="measure">Proposition Cedar Hollow East High School</span>
    </div>
    <div class="pillars-rule top"></div>
    <p class="pillars"><span>OUR CHILDREN</span><span>|</span><span>OUR DISTRICT</span><span>|</span><span>OUR FUTURE</span></p>
    <div class="pillars-rule bottom"></div>
    <p class="disclaimer">Advertisement paid for by the Cedar Hollow East High School Election Committee, Marla Kinney Treasurer.</p>
  </section>

  <section class="card-back" aria-label="Postcard back">
    <div class="school-photo" role="img" aria-label="Rendering of the proposed high school building"></div>
    <div class="social-mark" aria-label="Find us on social media"></div>
    <div class="stamp-box" aria-label="Postage area"></div>
    <div class="back-info">
      <h2 class="committee">Cedar Hollow East High School Election Committee</h2>
      <p class="purpose">For the creation of a Fairbrook R-V District High School</p>
      <p class="contact">Call Derek Holcomb @ 417-586-1047 or<br>Alan Pruitt @ 417-586-3390</p>
      <p class="note">for more information or to register<br>for an upcoming Q&amp;A forum.</p>
    </div>
    <p class="web">www.cedarhollowsample.com</p>
  </section>
</body>
</html>
```